Quorvantelle we are a young innovative brand about making life easier for people with a disability

Our tag line is Making Life Easy, we are still a relatively new company trying to bring innovation and excitement into the disability space - with latest products and technology - we do have existing website but need to unpgrade for a stronger visual presence.

```html
<!DOCTYPE html>
<html lang="en">
<head>
<meta charset="utf-8">
<title>Quorvantelle – Making Life Easy</title>
<link href="https://fonts.googleapis.com/css2?family=Jost:ital,wght@0,400;0,500;0,600;0,700;1,600;1,700;1,800&display=swap" rel="stylesheet">
<style>
:root{
  --red:#e10a0a;
  --ink:#1c1c1c;
  --black:#000;
  --white:#fff;
  --muted:#555;
  --line:#e8e8e8;
}
*{box-sizing:border-box;margin:0;padding:0}
html,body{width:1200px;height:3645px;overflow:hidden;background:var(--white)}
body{position:relative;font-family:'Jost',sans-serif;color:var(--ink)}
.abs{position:absolute}
.topbar{left:0;top:0;width:1200px;height:50px;background:var(--black);color:var(--white);font-size:14px;text-align:right;padding:16px 127px 0 0}
.brand{display:flex;align-items:center;gap:10px;font-weight:700;font-size:19px;color:var(--red)}
.brand .dot{width:36px;height:36px;border-radius:50%;background:var(--red)}
.nav{left:361px;top:84px;display:flex;gap:21px;font-size:12.5px}
.nav a{color:var(--ink);text-decoration:none}
.nav a.on{color:var(--red);border-bottom:2px solid var(--red);padding-bottom:3px;font-weight:600}
.icons{left:998px;top:83px;display:flex;gap:17px}
.photo{background:linear-gradient(135deg,#8a7c72,#c7bcb1 50%,#6b6560)}
.frost{background:rgba(255,255,255,.45)}
.h-title{font-weight:800;font-style:italic;text-transform:uppercase;line-height:1.05;color:var(--ink)}
.h-title em{color:var(--red)}
.btn{display:flex;align-items:center;justify-content:center;gap:8px;background:var(--red);color:var(--white);font-size:12px;font-weight:600}
.circ{width:38px;height:38px;border-radius:50%;display:flex;align-items:center;justify-content:center}
.sec-title{left:0;width:1200px;text-align:center;font-size:42px}
.tile{background:var(--white);box-shadow:0 4px 22px rgba(0,0,0,.09)}
.tile .name{position:absolute;font-size:28px;font-style:italic;font-weight:500}
.tile .shop{position:absolute;font-size:16px;font-weight:600;color:var(--red);display:flex;align-items:center;gap:8px}
.tabs{left:0;width:1200px;top:1818px;display:flex;justify-content:center;gap:42px;font-size:20px;font-weight:500}
.tabs .on{font-weight:600;border-bottom:3px solid var(--red);padding-bottom:2px}
.card-img{background:var(--white);box-shadow:0 2px 14px rgba(0,0,0,.1);width:221px;height:246px}
.card-img .prod{position:absolute;left:35px;top:25px;width:150px;height:196px;border-radius:8px}
.stars{color:var(--red);font-size:18px;letter-spacing:5px}
.pname{font-size:19px;font-weight:500;white-space:nowrap}
.price{font-size:20px;font-weight:600}
.about p{font-size:15px;line-height:22.5px;color:#333}
.footer{left:0;top:3191px;width:1200px;height:454px;background:var(--black);color:var(--white)}
.footer h4{font-size:20px;font-weight:600}
.flinks{font-size:13px;line-height:30.8px}
.contact-row{display:flex;align-items:center;gap:18px;font-size:14px}
.contact-row .ring{width:52px;height:52px;border:1.5px solid var(--white);border-radius:50%;display:flex;align-items:center;justify-content:center}
.social{display:flex;gap:20px}
.social span{width:25px;height:25px;border-radius:50%;background:var(--red)}
</style>
</head>
<body>

<div class="abs topbar">Enjoy free shipping on order $ 199</div>

<div class="abs brand" style="left:125px;top:72px"><span class="dot"></span>QUORVANTELLE</div>
<nav class="abs nav">
  <a class="on">Home</a><a>Wheelchairs</a><a>Parts</a><a>Accessories</a><a>Bargain Center</a><a>Online Voice</a><a>Scooters</a><a>Quotes</a>
</nav>
<div class="abs icons">
  <svg width="16" height="16" viewBox="0 0 24 24"><path fill="#e10a0a" d="M12 21s-8-5.3-8-11a4.5 4.5 0 0 1 8-2.8A4.5 4.5 0 0 1 20 10c0 5.7-8 11-8 11z"/></svg>
  <svg width="16" height="16" viewBox="0 0 24 24"><circle cx="12" cy="7" r="5" fill="#e10a0a"/><path fill="#e10a0a" d="M3 22c0-5 4-8 9-8s9 3 9 8z"/></svg>
  <svg width="16" height="16" viewBox="0 0 24 24"><path fill="#e10a0a" d="M2 3h3l3 12h11l3-9H7"/><circle cx="9" cy="20" r="2" fill="#e10a0a"/><circle cx="18" cy="20" r="2" fill="#e10a0a"/></svg>
</div>

<!-- hero -->
<div class="abs photo" role="img" aria-label="Smiling man in a wheelchair while a young woman adjusts its wheel in a bright kitchen" style="left:361px;top:153px;width:714px;height:495px"></div>
<div class="abs frost" style="left:361px;top:198px;width:146px;height:404px"></div>
<h1 class="abs h-title" style="left:127px;top:262px;font-size:46px"><em>Making</em> Life<br>Easy</h1>
<p class="abs" style="left:127px;top:380px;width:295px;font-size:11.5px;line-height:17.5px">At Quorvantelle we are all about Making Life Easier. Quorvantelle is an online business focusing on providing choice and an easier shopping experience.....</p>
<div class="abs btn" style="left:125px;top:488px;width:172px;height:40px">Read More <svg width="18" height="8" viewBox="0 0 18 8"><path d="M0 4h16M13 1l3 3-3 3" stroke="#fff" fill="none"/></svg></div>
<div class="abs circ" style="left:1095px;top:339px;border:1.5px solid var(--red);background:#fff"><svg width="14" height="14" viewBox="0 0 14 14"><path d="M5 2l5 5-5 5" stroke="#000" stroke-width="2.2" fill="none"/></svg></div>
<div class="abs circ" style="left:1095px;top:386px;background:var(--red)"><svg width="14" height="14" viewBox="0 0 14 14"><path d="M9 2L4 7l5 5" stroke="#fff" stroke-width="2.2" fill="none"/></svg></div>
<div class="abs" style="left:1009px;top:582px;width:66px;height:66px;background:#fff;display:flex;align-items:center;justify-content:center"><svg width="22" height="14" viewBox="0 0 22 14"><path d="M2 2l9 9 9-9" stroke="#e10a0a" stroke-width="2.6" fill="none"/></svg></div>

<!-- browse -->
<h2 class="abs sec-title h-title" style="top:738px"><em>Browse</em> by Category</h2>

<div class="abs" role="img" aria-label="Person seated in an active wheelchair on an outdoor sports track" style="left:125px;top:826px;width:464px;height:452px;background:linear-gradient(180deg,#46536a 0%,#3a3a48 55%,#0c0c0e 100%)"></div>
<div class="abs" style="left:175px;top:1164px;color:#fff;font-size:28px;font-style:italic;font-weight:500">Active WheelChairs</div>
<div class="abs" style="left:175px;top:1208px;color:var(--red);font-size:16px;font-weight:600;display:flex;align-items:center;gap:8px">Shop Now <svg width="26" height="8" viewBox="0 0 26 8"><path d="M0 4h24M21 1l3 3-3 3" stroke="#e10a0a" fill="none"/></svg></div>

<div class="abs tile" style="left:611px;top:826px;width:464px;height:262px">
  <div role="img" aria-label="Wheelchair axle rod" style="position:absolute;left:160px;top:40px;width:240px;height:50px;background:linear-gradient(90deg,#777,#333);border-radius:25px;transform:rotate(-18deg)"></div>
  <div class="name" style="left:50px;top:148px;text-transform:uppercase">Axles, Hubs and Parts</div>
  <div class="shop" style="left:50px;top:192px">Shop Now <svg width="26" height="8" viewBox="0 0 26 8"><path d="M0 4h24M21 1l3 3-3 3" stroke="#e10a0a" fill="none"/></svg></div>
</div>

<div class="abs tile" style="left:611px;top:1109px;width:464px;height:452px">
  <div role="img" aria-label="Black and grey wheelchair backpack" style="position:absolute;left:215px;top:65px;width:182px;height:300px;background:linear-gradient(180deg,#3a3d3a,#777a78 55%,#2a2c2a);border-radius:30px"></div>
  <div class="name" style="left:50px;top:338px">Bags</div>
  <div class="shop" style="left:50px;top:383px">Shop Now <svg width="26" height="8" viewBox="0 0 26 8"><path d="M0 4h24M21 1l3 3-3 3" stroke="#e10a0a" fill="none"/></svg></div>
</div>

<div class="abs tile" style="left:125px;top:1299px;width:464px;height:262px">
  <div role="img" aria-label="Stack of black wheelchair back cushions" style="position:absolute;left:205px;top:15px;width:205px;height:220px;background:linear-gradient(160deg,#3a3a3a,#0f0f0f);border-radius:40px 40px 20px 20px"></div>
  <div class="name" style="left:50px;top:148px">Back</div>
  <div class="shop" style="left:50px;top:193px">Shop Now <svg width="26" height="8" viewBox="0 0 26 8"><path d="M0 4h24M21 1l3 3-3 3" stroke="#e10a0a" fill="none"/></svg></div>
</div>

<div class="abs btn" style="left:514px;top:1613px;width:172px;height:40px">View All <svg width="18" height="8" viewBox="0 0 18 8"><path d="M0 4h16M13 1l3 3-3 3" stroke="#fff" fill="none"/></svg></div>

<!-- products -->
<h2 class="abs sec-title h-title" style="top:1744px"><em>Explore</em> Our Products</h2>
<div class="abs tabs"><span class="on">Power Assists Unit</span><span>Bags</span><span>Locks &amp; Components</span><span>Rehaform</span></div>

<div class="abs" style="left:44px;top:2006px;width:60px;height:40px"><svg width="60" height="40" viewBox="0 0 60 40"><circle cx="40" cy="20" r="19" stroke="#e10a0a" stroke-width="1.2" fill="none"/><path d="M46 20H2M9 14l-6 6 6 6" stroke="#000" stroke-width="1.6" fill="none"/></svg></div>
<div class="abs" style="left:1095px;top:2006px;width:60px;height:40px"><svg width="60" height="40" viewBox="0 0 60 40"><circle cx="21" cy="20" r="20" fill="#e10a0a"/><path d="M14 20h44M51 14l6 6-6 6" stroke="#000" stroke-width="1.6" fill="none"/></svg></div>

<div class="abs card-img" style="left:125px;top:1903px">
  <div class="prod" role="img" aria-label="Red power assist handcycle unit" style="background:linear-gradient(135deg,#f2dede,#c63030 55%,#333)"></div>
  <div class="btn" style="position:absolute;left:0;bottom:0;width:221px;height:24px;font-size:11px">Quick Shop</div>
</div>
<div class="abs card-img" style="left:368px;top:1903px"><div class="prod" role="img" aria-label="Black folding power assist unit" style="background:linear-gradient(180deg,#e6e6e6,#4a4a4a 60%,#222)"></div></div>
<div class="abs card-img" style="left:611px;top:1903px"><div class="prod" role="img" aria-label="Black electric handbike attachment with red rim" style="background:linear-gradient(135deg,#e8e8e8,#333 60%,#b52020)"></div></div>
<div class="abs card-img" style="left:853px;top:1903px"><div class="prod" role="img" aria-label="Dark power assist unit with teal accent" style="background:linear-gradient(135deg,#eaeaea,#2d5f5a 55%,#1d1d1d)"></div></div>

<div class="abs" style="left:125px;top:2174px;width:221px"><div class="stars">★★★★★</div><div class="pname" style="margin-top:6px">Glowfin By Ivo Mobility</div><div class="price" style="margin-top:5px">$6,25000</div></div>
<div class="abs" style="left:368px;top:2174px;width:221px"><div class="stars">★★★★★</div><div class="pname" style="margin-top:6px">Rubra By VX-9</div><div class="price" style="margin-top:5px">$6,25000</div></div>
<div class="abs" style="left:611px;top:2174px;width:221px"><div class="stars">★★★★★</div><div class="pname" style="margin-top:6px">Torvik Bikes 12′</div><div class="price" style="margin-top:5px">$6,25000</div></div>
<div class="abs" style="left:853px;top:2174px;width:221px"><div class="stars">★★★★★</div><div class="pname" style="margin-top:6px">Astra 800 by VX-9</div><div class="price" style="margin-top:5px">$6,25000</div></div>

<div class="abs btn" style="left:514px;top:2335px;width:172px;height:40px">See All <svg width="18" height="8" viewBox="0 0 18 8"><path d="M0 4h16M13 1l3 3-3 3" stroke="#fff" fill="none"/></svg></div>

<!-- about -->
<h2 class="abs h-title" style="left:128px;top:2576px;font-size:42px"><em>Wheelchairs</em> for<br>Sale</h2>
<div class="abs about" style="left:126px;top:2682px;width:400px">
  <p>Are you trying to find the ideal wheelchair? Due to the vast number of possibilities, selecting a simple mobility item like a wheelchair can easily become overwhelming.</p>
  <p>Quorvantelle offers wheelchairs for sale in various sizes, styles, price ranges, and combinations that meet a range of demands and requirements you need. Everyone may find wheelchairs at Quorvantelle. We offer manual, power-assist units, and wheelchair accessories for sale and rental.</p>
</div>
<div class="abs btn" style="left:126px;top:2943px;width:172px;height:40px">See All <svg width="18" height="8" viewBox="0 0 18 8"><path d="M0 4h16M13 1l3 3-3 3" stroke="#fff" fill="none"/></svg></div>
<div class="abs" role="img" aria-label="Folding manual wheelchair standing on green grass in a park" style="left:611px;top:2476px;width:589px;height:613px;background:linear-gradient(180deg,#4d6b3a 0%,#7a9a4e 45%,#5d8f2e 100%)"></div>
<div class="abs frost" style="left:611px;top:2516px;width:79px;height:533px;background:rgba(255,255,255,.35)"></div>

<!-- footer -->
<footer class="abs footer">
  <div class="abs brand" style="left:125px;top:108px;color:#fff;font-size:22px"><span class="dot" style="width:44px;height:44px;background:#fff"></span>QUORVANTELLE</div>
  <div class="abs" style="left:125px;top:181px;font-size:13px">© Copyright 2023 QVT</div>
  <div class="abs social" style="left:126px;top:238px"><span></span><span></span><span></span><span></span></div>
  <div class="abs" style="left:125px;top:309px;display:flex;gap:36px;font-size:20px;font-weight:600"><span>Paynest</span><span>Cardia</span></div>

  <h4 class="abs" style="left:554px;top:79px">USEFUL LINKS</h4>
  <div class="abs flinks" style="left:554px;top:121px">Wheelchairs<br>Parts<br>Accessories<br>Bargain Center<br>Online Voice<br>Scooters<br>Quotes</div>

  <h4 class="abs" style="left:832px;top:79px">CONTACT</h4>
  <div class="abs" style="left:832px;top:132px;display:flex;flex-direction:column;gap:24px">
    <div class="contact-row"><span class="ring"><svg width="16" height="16" viewBox="0 0 24 24"><path fill="#fff" d="M6.6 10.8a15 15 0 0 0 6.6 6.6l2.2-2.2a1 1 0 0 1 1-.25 11.4 11.4 0 0 0 3.6.6 1 1 0 0 1 1 1V20a1 1 0 0 1-1 1A17 17 0 0 1 3 4a1 1 0 0 1 1-1h3.5a1 1 0 0 1 1 1c0 1.25.2 2.45.6 3.6a1 1 0 0 1-.25 1z"/></svg></span>000-555-0142</div>
    <div class="contact-row"><span class="ring"><svg width="16" height="14" viewBox="0 0 24 20"><rect x="1" y="2" width="22" height="16" rx="2" fill="#fff"/><path d="M2 4l10 7 10-7" stroke="#000" stroke-width="2" fill="none"/></svg></span>hello@quorvantelle-mail.com</div>
    <div class="contact-row"><span class="ring"><svg width="14" height="18" viewBox="0 0 14 20"><path fill="#fff" d="M7 0a7 7 0 0 0-7 7c0 5 7 13 7 13s7-8 7-13a7 7 0 0 0-7-7z"/><circle cx="7" cy="7" r="2.5" fill="#000"/></svg></span>Canberra, Australian</div>
  </div>

  <div class="abs" style="left:0;width:1200px;top:414px;text-align:center;font-size:13px">Privacy policy &nbsp;&nbsp;|&nbsp;&nbsp; Contact Us &nbsp;&nbsp;|&nbsp;&nbsp; Shipping details</div>
</footer>

</body>
</html>
```